90 Day Landing Page for Online Coaching

Need a website design that’s gonna be used for an online coaching landing page (details in the WORD document). The colors/design can be complimentary to the program called, The Harvest Ledger Method; the banners are attached in the document
There are alot of extra photos that you can use but none of them are required; use as needed.
We don’t have the URL yet, but we intend to use a single landing page.

Target Market(s)

for men and women looking to launch a business

Industry/Entity Type

business consulting

Requirements
Must have
• the copy attached

```html
<!DOCTYPE html>
<html lang="en">
<head>
<meta charset="utf-8">
<title>The Harvest Ledger Method – 90 Day Launch</title>
<link href="https://fonts.googleapis.com/css2?family=Bitter:wght@400;500;600&family=Inter:wght@400;500;600;700&display=swap" rel="stylesheet">
<style>
:root{
  --blue:#0b4c97;
  --blue-deep:#083d7d;
  --accent:#3d8ef2;
  --cyan:#cdf3f7;
  --ice:#eef6fd;
  --ink:#1c2430;
  --muted:#6b7480;
  --line:#3d7fe0;
  --orange:#f5a524;
  --green:#27b26a;
  --card:#ffffff;
  --photo-a:#8a7a6c;
  --photo-b:#2f3848;
}
*{box-sizing:border-box;margin:0;padding:0}
html,body{width:1200px;height:1200px;overflow:hidden;background:#fff}
body{font-family:"Inter",sans-serif;color:var(--ink);position:relative}
.page{position:absolute;left:505px;top:0;width:1000px;height:7460px;transform:scale(.1609);transform-origin:0 0;background:#fff;overflow:hidden}
section{position:relative;overflow:hidden}
.serif{font-family:"Bitter",serif}
h2{font-family:"Bitter",serif;font-weight:500;font-size:34px;line-height:1.25}
h2 em,h1 em{font-style:normal;color:var(--accent)}
.tag{display:inline-block;background:#111;color:#fff;font-size:11px;padding:3px 10px;border-radius:4px;font-weight:600;letter-spacing:.5px}
.photo{border-radius:14px;background:linear-gradient(160deg,var(--photo-a),var(--photo-b))}
.small{font-size:13px;line-height:1.5;color:var(--muted)}
.btn{display:inline-block;background:var(--orange);color:#fff;font-weight:700;font-size:15px;padding:12px 26px;border-radius:8px}
.frame{position:absolute;border:4px solid var(--line);border-radius:28px}

/* hero */
.hero{height:567px;background:#fff}
.nav{position:absolute;left:80px;top:20px;right:80px;display:flex;align-items:center;justify-content:space-between}
.brand{font-family:"Bitter",serif;font-weight:600;font-size:18px;color:var(--blue-deep);width:150px;line-height:1.1}
.menu{display:flex;gap:14px;font-size:10px;background:#fff;padding:8px 12px;border-radius:8px;box-shadow:0 2px 10px rgba(0,0,0,.1)}
.menu span:first-child{background:#111;color:#fff;padding:2px 8px;border-radius:4px}
.hero-side{position:absolute;left:560px;top:0;width:440px;height:567px;background:linear-gradient(180deg,var(--blue),var(--blue-deep))}
.hero h1{position:absolute;left:85px;top:110px;font-family:"Bitter",serif;font-weight:400;font-size:40px;line-height:1.28;width:480px}
.hero .lede{position:absolute;left:85px;top:275px;width:420px}
.gallery{position:absolute;left:85px;top:355px}
.gallery .row{display:flex;gap:14px;margin-top:14px;align-items:flex-end}
.banner{position:absolute;left:605px;top:120px;width:310px;height:315px;border:3px solid #6fb0ff;border-radius:14px;background:linear-gradient(160deg,#1e6fd0,#0a3e7f);color:#fff;text-align:center;padding:20px}
.banner .t{font-family:"Bitter",serif;font-weight:600;font-size:22px;line-height:1.1}
.banner .ph{height:130px;margin:14px 0;border-radius:10px;background:linear-gradient(180deg,#5d6d84,#23324a)}
.banner .s{font-weight:700;font-size:17px;color:#ffd86b}
.stats{position:absolute;left:605px;top:470px;width:340px;display:flex;justify-content:space-between;color:#fff}
.stats b{display:block;font-size:17px;font-weight:500}
.stats span{font-size:10px;opacity:.7}
.vert{position:absolute;right:10px;top:40px;writing-mode:vertical-rl;font-family:"Bitter",serif;font-size:56px;color:rgba(255,255,255,.12)}

/* problem */
.problem{height:553px;background:linear-gradient(90deg,var(--cyan),#f4f6f7 45%,#f4f6f7)}
.bubbles{position:absolute;left:120px;top:100px;width:400px;height:400px}
.bubble{position:absolute;width:100px;background:#fff;border-radius:8px;padding:8px;font-size:8px;line-height:1.35;box-shadow:0 3px 10px rgba(0,0,0,.08)}
.hub{position:absolute;left:165px;top:170px;width:70px;height:70px;border-radius:50%;background:linear-gradient(160deg,#6a7b92,#25324a);border:4px solid #fff}
.story-photo{position:absolute;left:520px;top:130px;width:210px;height:390px}
.story{position:absolute;left:630px;top:250px;width:285px;background:#fff;border-radius:12px;padding:20px;box-shadow:0 6px 20px rgba(0,0,0,.1)}
.story h3{font-family:"Bitter",serif;font-weight:500;font-size:19px;line-height:1.3;margin-bottom:10px}

/* outcomes */
.outcomes{height:667px;background:linear-gradient(90deg,var(--cyan),#fff 40%,#fff 70%,#e4f1fc)}
.outcomes .head{text-align:center;padding-top:28px}
.checks{position:absolute;top:110px;display:grid;grid-template-columns:1fr 1fr;gap:14px}
.check{background:#fff;border-radius:8px;padding:10px 10px 10px 30px;font-size:9px;line-height:1.4;position:relative;box-shadow:0 2px 8px rgba(0,0,0,.07);min-height:70px}
.check:before{content:"";position:absolute;left:10px;top:12px;width:11px;height:11px;border-radius:50%;background:var(--green)}
.center-photo{position:absolute;left:395px;top:95px;width:210px;height:180px;border:4px solid var(--line);border-radius:10px;padding:8px;background:#fff}
.center-photo div{height:100%;border-radius:6px;background:linear-gradient(160deg,#9b6f58,#2b3446)}
.testi{position:absolute;left:85px;top:335px;width:830px;height:250px;border:4px solid var(--line);border-radius:24px;background:linear-gradient(90deg,#e6f8fb,#fff)}
.testi .face{position:absolute;left:105px;top:28px;width:180px;height:180px;border-radius:50%;background:linear-gradient(160deg,#c14a57,#3b2530)}
.testi .txt{position:absolute;left:415px;top:28px;width:360px}
.testi .txt h3{font-family:"Bitter",serif;font-weight:500;font-size:19px;margin:6px 0}
.arrow{position:absolute;top:112px;width:26px;height:26px;border-radius:50%;border:1px solid #bcc8d6;background:#fff}
.dots{position:absolute;left:258px;bottom:24px;display:flex;gap:6px}
.dots i{width:6px;height:6px;border-radius:50%;background:#b8c4d2}
.dots i:first-child{background:var(--blue)}

/* cta band */
.cta-band{height:290px;background:var(--blue)}
.cta-card{position:absolute;left:95px;top:65px;width:815px;height:175px;border-radius:14px;background:linear-gradient(90deg,#fff 55%,#a8cdfb 80%,#5d9cf0)}
.cta-card p{position:absolute;left:70px;top:36px;width:450px;text-align:center;font-family:"Bitter",serif;font-size:20px;line-height:1.35}
.cta-card p em{font-style:normal;color:var(--green)}
.mini-banner{position:absolute;left:45px;top:115px;width:270px;height:40px;border-radius:4px;background:linear-gradient(90deg,#0a3e7f,#1e6fd0);color:#fff;font-size:10px;font-weight:700;padding:12px 14px}
.cta-card .btn{position:absolute;left:415px;top:113px;font-size:12px;padding:10px 18px}
.standing{position:absolute;left:650px;top:-10px;width:160px;height:250px;border-radius:80px 80px 0 0;background:linear-gradient(180deg,#4a3b38,#1b1d24)}

/* killers */
.killers{height:502px;background:linear-gradient(90deg,#fff,var(--ice) 50%,#dff2fb)}
.killer{position:absolute;top:135px;width:225px;background:#fff;border-radius:10px;box-shadow:0 4px 14px rgba(0,0,0,.08);overflow:hidden}
.killer .ph{height:140px;background:linear-gradient(160deg,#a3a8b0,#4a5361)}
.killer .b{padding:12px;font-size:9px;line-height:1.45;color:var(--muted)}
.killer h4{font-family:"Bitter",serif;font-weight:500;color:var(--ink);font-size:12px;margin:6px 0}

/* experts */
.experts{height:1216px;background:var(--blue);color:#fff}
.experts .head{text-align:center;padding-top:40px}
.tabs{display:flex;justify-content:center;margin-top:18px}
.tabs div{border:2px solid #fff;padding:8px 18px;font-size:15px}
.tabs div:first-child{background:#fff;color:var(--ink)}
.creds{position:absolute;left:125px;top:160px;width:750px;display:grid;grid-template-columns:repeat(3,1fr);gap:12px}
.cred{background:#fff;color:var(--ink);border-radius:8px;padding:12px 12px 12px 44px;font-size:8px;line-height:1.4;height:96px;position:relative}
.cred:before{content:"";position:absolute;left:12px;top:14px;width:22px;height:22px;border-radius:4px;background:#dbe3ee}
.press{position:absolute;left:125px;top:380px;width:750px;height:52px;background:#fff;border-radius:8px;display:flex;justify-content:space-around;align-items:center}
.press i{width:60px;height:16px;border-radius:3px;background:#c4ccd6}
.collage{position:absolute;left:125px;top:460px;width:750px;height:355px;display:grid;grid-template-columns:1fr 1.2fr 1fr;gap:6px}
.collage div{border-radius:4px}
.col{display:grid;gap:6px}
.review{position:absolute;left:85px;top:890px;width:830px;height:275px;border:4px solid #5ea2ff;border-radius:22px;background:linear-gradient(135deg,#0f5fbd,#0a4b97)}
.review .face{position:absolute;left:105px;top:38px;width:180px;height:180px;border-radius:50%;background:linear-gradient(160deg,#8b5a3f,#2a1e1a)}
.review .txt{position:absolute;left:370px;top:34px;width:420px;font-size:10px;line-height:1.5;opacity:.9}
.review h3{font-family:"Bitter",serif;font-size:17px;font-weight:500;margin:6px 0 10px}

/* includes */
.includes{height:810px;background:linear-gradient(180deg,#e6f4fc,#fff 40%,#fff 80%,#e9f3fc)}
.includes .head{text-align:center;padding-top:42px}
.grid4{position:absolute;left:110px;top:112px;width:780px;display:grid;grid-template-columns:repeat(4,1fr);gap:12px}
.item{background:#fff;border-radius:8px;padding:12px;box-shadow:0 3px 10px rgba(0,0,0,.06);height:120px;font-size:8px;line-height:1.4;color:var(--muted)}
.item.tall{height:165px}
.item h4{font-size:10px;color:var(--ink);font-weight:600;margin:0 0 6px 32px;position:relative}
.item h4:before{content:"";position:absolute;left:-32px;top:0;width:22px;height:22px;border-radius:4px;background:#d9e5f3}
.launch{position:absolute;left:110px;top:615px;width:780px;height:170px;border-radius:10px;background:linear-gradient(90deg,#fff 60%,#9cc6fb 85%,#5f9cf0);box-shadow:0 6px 18px rgba(0,0,0,.08)}
.launch p{position:absolute;left:40px;top:30px;width:460px;text-align:center;font-family:"Bitter",serif;font-size:19px;line-height:1.35}
.launch p em{font-style:normal;color:var(--orange)}
.facts{position:absolute;left:50px;top:100px;display:flex;gap:40px;font-size:9px;color:var(--muted)}
.facts b{display:block;color:var(--green);font-size:16px;margin-top:4px}

/* videos */
.videos{height:510px;background:linear-gradient(90deg,#fff 60%,#dff3fa)}
.video{position:absolute;top:150px;width:215px}
.video .ph{height:125px;border-radius:6px;background:linear-gradient(160deg,#8b7663,#2f3340);position:relative}
.video .ph:after{content:"";position:absolute;left:92px;top:47px;width:30px;height:30px;border-radius:50%;background:rgba(255,255,255,.8)}
.video p{font-size:11px;line-height:1.4;margin-top:12px}

/* biz types */
.biz{height:870px;background:linear-gradient(180deg,#dcecfb,#e8f2fc 60%,#e3eefb)}
.biz .head{text-align:center;padding-top:30px}
.types{position:absolute;top:130px;font-size:9px;line-height:1.4}
.types div{margin-bottom:26px}
.types b{font-size:10px}
.hub-banner{position:absolute;left:418px;top:150px;width:165px;height:170px;border-radius:8px;background:linear-gradient(160deg,#1e6fd0,#0a3e7f);border:3px solid #8bc0ff;color:#fff;text-align:center;padding:10px;font-family:"Bitter",serif;font-size:12px;font-weight:600}
.quotes{position:absolute;left:120px;width:760px;display:grid;grid-template-columns:repeat(3,1fr);gap:30px}
.quote{background:#fff;border-radius:8px;padding:18px;height:225px;font-size:9px;line-height:1.5;color:var(--muted)}
.quote .q{font-family:"Bitter",serif;font-size:30px;color:var(--accent);line-height:.8;height:24px}

/* faq + close */
.faq{height:545px;background:var(--blue);color:#fff}
.faq-box{position:absolute;left:140px;top:28px;width:720px;height:450px;border:3px solid #5ea2ff;border-radius:12px;padding:50px 40px 0}
.faq-box h2{text-align:center;font-size:24px;margin:8px 0 30px}
.faq-q{background:#fff;color:var(--ink);border-radius:4px;padding:9px 14px 9px 40px;font-size:11px;font-weight:600;margin-bottom:12px;position:relative}
.faq-q:before{content:"";position:absolute;left:14px;top:9px;width:12px;height:12px;border-radius:50%;border:1.5px solid #9fb0c5}
.faq-q small{display:block;font-weight:400;font-size:9px;color:var(--muted);margin-top:10px}
.close{height:930px;background:linear-gradient(180deg,#fff,#eaf3fd 50%,#fff)}
.offer{position:absolute;left:110px;top:10px;width:780px;height:215px;border-radius:10px;background:linear-gradient(90deg,#fff 35%,#eaf6fb 50%,#fff 60%,#a9cffb);box-shadow:0 6px 18px rgba(0,0,0,.08)}
.offer p{position:absolute;left:25px;top:28px;width:280px;text-align:center;font-family:"Bitter",serif;font-size:19px;line-height:1.35}
.offer p em{font-style:normal;color:var(--green)}
.cards{position:absolute;left:30px;top:160px;display:flex;gap:12px}
.cards i{width:50px;height:28px;border-radius:4px;background:#c8d3e0}
.price{position:absolute;left:585px;top:55px;font-family:"Bitter",serif;font-size:16px;line-height:1.4;text-align:center}
.price b{color:#e23b3b;font-weight:500}
.offer .yes{position:absolute;left:615px;top:150px;font-weight:700;font-size:15px}
.offer .btn{position:absolute;left:725px;top:140px;font-size:10px;padding:10px 14px}
.standing2{position:absolute;left:420px;top:-30px;width:150px;height:245px;border-radius:75px 75px 0 0;background:linear-gradient(180deg,#4a3b38,#1b1d24)}
.footer{position:absolute;left:80px;top:665px;width:850px;height:260px}
.footer .links{position:absolute;left:560px;top:12px;display:grid;grid-template-columns:1fr 1fr;gap:14px 60px;font-size:9px;color:var(--muted)}
.foot-banner{position:absolute;left:330px;top:0;width:175px;height:200px;border-radius:8px;background:linear-gradient(160deg,#1e6fd0,#0a3e7f);border:3px solid #8bc0ff;color:#fff;text-align:center;font-family:"Bitter",serif;font-size:12px;font-weight:600;padding:12px}
</style>
</head>
<body>
<main class="page">

  <!-- HERO -->
  <section class="hero">
    <div class="hero-side"><div class="vert">HARVEST LEDGER</div></div>
    <div class="nav">
      <div class="brand">The Harvest Ledger Method</div>
      <div class="menu"><span>Home</span><span>Motivation</span><span>Our Mission</span><span>Meet Us</span><span>Tips</span><span>Meet Experts</span><span>Get Inspired</span><span>What You Get</span><span>Real Results</span><span>FAQ</span></div>
    </div>
    <h1>It's Your <em>Turn!</em><br>The Launch a Million Dollar Brand in 90 Days!</h1>
    <p class="lede small">Is a 90-Days Sprint that helps you turn your idea, skill, or passion into a brand that makes money – fast.</p>
    <div class="gallery">
      <div class="serif" style="font-size:15px">Our <span style="color:var(--accent)">Gallery</span></div>
      <div class="row">
        <div class="photo" role="img" aria-label="Video still of the hosts on stage" style="width:205px;height:140px"></div>
        <div class="photo" role="img" aria-label="Photo of the two hosts" style="width:95px;height:85px"></div>
        <div class="photo" role="img" aria-label="More gallery photos" style="width:95px;height:85px;display:flex;align-items:center;justify-content:center;color:#fff;font-weight:700;font-size:22px">10+</div>
      </div>
    </div>
    <div class="banner">
      <div class="t">THE HARVEST LEDGER METHOD</div>
      <div class="ph" role="img" aria-label="Portrait of the two program hosts"></div>
      <div class="s">LAUNCH A MILLION DOLLAR BRAND IN 90 DAYS</div>
      <div style="margin-top:10px;font-size:11px;font-weight:700">SIGN UP TODAY!</div>
    </div>
    <div class="stats">
      <div><b>10 Years</b><span>Experience</span></div>
      <div><b>99.8%</b><span>Satisfaction</span></div>
      <div><b>250+</b><span>Clients</span></div>
    </div>
  </section>

  <!-- PROBLEM -->
  <section class="problem">
    <div class="frame" style="left:85px;top:58px;width:475px;height:470px;border-top-right-radius:28px;border-color:var(--line)"></div>
    <div style="position:absolute;left:120px;top:118px"><span class="tag">MOTIVATION</span><h2 style="font-size:17px;margin-top:6px">Does This Sound <em>Like You</em>?</h2></div>
    <div class="bubbles">
      <div class="bubble" style="left:40px;top:60px">You want to escape the nine-to-five and build real freedom.</div>
      <div class="bubble" style="left:200px;top:60px">You have good ideas but never finish what you start.</div>
      <div class="bubble" style="left:0;top:160px">You feel stuck while others seem to move ahead fast.</div>
      <div class="bubble" style="left:240px;top:170px">You keep waiting for the perfect time to begin.</div>
      <div class="bubble" style="left:10px;top:260px">You're tired of guessing what works online.</div>
      <div class="bubble" style="left:235px;top:275px">You want a brand that pays you every month.</div>
      <div class="bubble" style="left:130px;top:310px">You need a clear plan and someone to guide you.</div>
      <div class="hub" role="img" aria-label="Portrait of a thoughtful founder"></div>
    </div>
    <div class="frame" style="left:540px;top:85px;width:260px;height:120px;border-bottom:none"></div>
    <div class="story-photo photo" role="img" aria-label="Host standing beside a car"></div>
    <div class="story">
      <h3>You're <em style="font-style:normal;color:var(--accent)">Not Alone</em>. I've Been There Too.</h3>
      <p class="small" style="font-size:9px">I know how it feels to have a dream but no map. I spent years testing ideas, losing money and starting over before I found a simple system that turned a small idea into a thriving brand.</p>
      <p class="small" style="font-size:9px;margin-top:10px">That is why I built this 90-day program: to help people like you skip the guessing and start earning sooner.</p>
    </div>
  </section>

  <!-- OUTCOMES -->
  <section class="outcomes">
    <div class="head"><span class="tag">OUR MISSION</span><h2 style="font-size:17px;margin-top:6px">By The End of <em>This Program</em>, You'll:</h2></div>
    <div class="checks" style="left:85px;width:290px">
      <div class="check">Have a fully launched business with paying customers.</div>
      <div class="check">Have the skills and knowledge to keep growing your brand.</div>
      <div class="check">Have sales and marketing systems that bring buyers in.</div>
      <div class="check">Be ready for the next level of your income goals.</div>
    </div>
    <div class="center-photo"><div role="img" aria-label="Photo of the two hosts together"></div></div>
    <div class="checks" style="left:630px;width:290px">
      <div class="check">Gain confidence and clarity about your business strategy.</div>
      <div class="check">Know how to grow a loyal audience on social media.</div>
      <div class="check">Be one step closer to financial freedom and wealth.</div>
      <div class="check">Make consistent income by following proven steps.</div>
    </div>
    <div class="testi">
      <div class="arrow" style="left:30px"></div><div class="arrow" style="right:30px"></div>
      <div class="face" role="img" aria-label="Portrait of a smiling graduate"></div>
      <div class="txt">
        <span class="tag">REAL RESULTS</span>
        <h3>See What's Possible When You <em style="font-style:normal;color:var(--accent)">Take Action</em></h3>
        <p class="small" style="font-size:9px">Thanks to the daily training and assignments, I am reaching more buyers than ever before and my brand finally feels real.</p>
        <p class="small" style="font-size:9px;margin-top:8px">I honestly never thought I could do it in 90 days. The plan was simple, the calls kept me on track and I made my first sales in week six.</p>
        <p style="font-size:8px;margin-top:10px">– GRADUATE</p>
      </div>
      <div class="dots"><i></i><i></i><i></i><i></i></div>
    </div>
  </section>

  <!-- CTA BAND -->
  <section class="cta-band">
    <div class="cta-card">
      <p>Enrollment closes soon. Secure your spot now and start building your future! <em>Join Now for 50% OFF</em></p>
      <div class="mini-banner">THE HARVEST LEDGER METHOD</div>
      <span class="btn">Add to Cart</span>
      <div class="standing" role="img" aria-label="Host waving"></div>
    </div>
  </section>

  <!-- KILLERS -->
  <section class="killers">
    <div class="frame" style="left:85px;top:-20px;width:380px;height:500px;border-top:none;border-right:none;border-top-left-radius:0"></div>
    <div class="frame" style="left:455px;top:48px;width:460px;height:390px"></div>
    <div style="position:absolute;left:150px;top:45px"><span class="tag">TIPS</span><h2 style="font-size:16px;margin-top:6px">There are <em>3 Killers</em> Of A<br>Great Business:</h2></div>
    <p class="small" style="position:absolute;left:505px;top:70px;width:340px;font-size:9px">Find out why businesses fail and master the strategies to overcome challenges and succeed faster than ever!</p>
    <div class="killer" style="left:150px"><div class="ph" role="img" aria-label="Stressed person thinking"></div><div class="b"><span class="tag" style="font-size:7px;background:#e8edf3;color:#333">Mistake</span><h4>Overthinking the First Step</h4>The longer you plan, the less you launch. Success comes from moving and adjusting, not waiting.</div></div>
    <div class="killer" style="left:390px;top:145px"><div class="ph" role="img" aria-label="Sketched plans on paper"></div><div class="b"><span class="tag" style="font-size:7px;background:#e8edf3;color:#333">Mistake</span><h4>Waiting for the "Perfect" Time</h4>Perfect never arrives. Every day you wait is a missed chance to learn and earn.</div></div>
    <div class="killer" style="left:630px;top:145px"><div class="ph" role="img" aria-label="Laptop showing an online store"></div><div class="b"><span class="tag" style="font-size:7px;background:#e8edf3;color:#333">Mistake</span><h4>Avoiding Sales and Marketing</h4>You can't grow if no one knows you exist. Learn to sell with confidence.</div></div>
  </section>

  <!-- EXPERTS -->
  <section class="experts">
    <div class="head"><span class="tag" style="background:#fff;color:#111">MEET EXPERTS</span><h2 style="font-size:17px;margin-top:6px">Their knowledge will make your <em>business grow rapidly</em></h2>
      <div class="tabs"><div>Meet Jada Moore</div><div>Meet Terrence "TR" Wells</div></div></div>
    <div class="creds">
      <div class="cred"><b>Best-Selling Author</b> of a wellness book series read by millions around the world.</div>
      <div class="cred"><b>Personal Brand Leader</b> with a large online following built from scratch.</div>
      <div class="cred"><b>Co-Founder</b> of a fast growing supplement brand sold in many stores.</div>
      <div class="cred"><b>National TV Guest</b> on daytime talk shows and morning news programs.</div>
      <div class="cred"><b>Celebrity Trainer</b> who has coached public figures and athletes.</div>
      <div class="cred"><b>Product Developer</b> who turned simple ideas into top selling lines.</div>
    </div>
    <div class="press" role="img" aria-label="Press feature badges"><i></i><i></i><i></i><i></i><i></i><i></i><i></i><i></i></div>
    <div class="collage">
      <div class="col"><div class="photo" role="img" aria-label="Host with a guest" style="background:linear-gradient(160deg,#9b7b62,#3a3034)"></div><div class="photo" role="img" aria-label="Host with a TV presenter" style="background:linear-gradient(160deg,#c26a58,#3a2a30)"></div></div>
      <div class="photo" role="img" aria-label="Hosts at a media event" style="background:linear-gradient(160deg,#b33a3a,#1f2230)"></div>
      <div class="col"><div class="photo" role="img" aria-label="Host on a TV set" style="background:linear-gradient(160deg,#3e8fb5,#3a2f34)"></div><div class="photo" role="img" aria-label="Host in a studio interview" style="background:linear-gradient(160deg,#4f87a8,#a8483e)"></div></div>
    </div>
    <div class="review">
      <div class="arrow" style="left:30px;top:125px;background:transparent;border-color:#6aa6ec"></div><div class="arrow" style="right:30px;top:125px;background:transparent;border-color:#6aa6ec"></div>
      <div class="face" role="img" aria-label="Portrait of a graduate in a suit"></div>
      <div class="txt"><span class="tag">REAL RESULTS</span>
        <h3>How People Just Like You Built <span style="color:#7fb8ff">Wealth and Freedom</span></h3>
        <p>I was a father with a steady job but no plan for more. Within three months I had a product, a simple store and a list of buyers who came back every week.</p>
        <p style="margin-top:8px">Each weekly call kept me focused. <b>Six months later my side business now earns more than my old salary</b> and I finally have time for my family.</p>
        <p style="margin-top:10px;font-size:8px">– GRADUATE</p></div>
      <div class="dots" style="bottom:20px"><i style="background:#fff"></i><i></i><i></i></div>
    </div>
  </section>

  <!-- INCLUDES -->
  <section class="includes">
    <div class="head"><span class="tag">WHAT YOU GET</span><h2 style="font-size:17px;margin-top:6px">Here's <em>EVERYTHING YOU GET</em> with the 90 Day Launch Course:</h2></div>
    <div class="grid4">
      <div class="item"><h4>Paying Customers on Hand</h4>Learn how to find and keep your first buyers quickly.</div>
      <div class="item"><h4>The 90-Day Business Blueprint</h4>A clear step by step plan that takes you from idea to launch.</div>
      <div class="item"><h4>A Fully Launched Business</h4>Finish the program with a live brand ready to sell.</div>
      <div class="item"><h4>Paying Customers on Hand</h4>Marketing systems that keep new buyers coming in.</div>
      <div class="item"><h4>Weekly Actionable Tasks and Assignments</h4>Small weekly goals keep you moving forward.</div>
      <div class="item"><h4>Private Member Community</h4>Connect with others on the same journey for support.</div>
      <div class="item"><h4>Done-For-You Template</h4>Plug in ready files for offers, pages and emails.</div>
      <div class="item"><h4>12-Month Growth Roadmap</h4>Know what to do after launch to keep growing.</div>
      <div class="item tall"><h4>Powered by AI Training for Entrepreneurs</h4>Use smart tools to save hours on content, research and planning every week.</div>
      <div class="item tall"><h4>Proven and Repeatable Systems for Success</h4>Simple systems you can repeat for every new product.</div>
      <div class="item tall"><h4>Weekly LIVE Coaching Videos and Demos with Jada & TR</h4>Get answers and feedback every week.</div>
      <div class="item"><h4>Confidence in Your Business</h4>Walk away ready to lead your brand with pride.</div>
    </div>
    <div class="launch">
      <p>This isn't just a course; it's a launch pad for your future business. <em>Key Details &amp; Timeline:</em></p>
      <div class="facts"><div>Program length<b>90 Days</b></div><div>Live Sessions<b>Weekly, 2 hours each</b></div><div>Dates<b>Feb 17th – May 18th</b></div></div>
      <div class="standing" role="img" aria-label="Host standing with arms crossed" style="left:560px;top:-40px;height:210px"></div>
    </div>
  </section>

  <!-- VIDEOS -->
  <section class="videos">
    <div class="frame" style="left:85px;top:40px;width:420px;height:440px;border-right:none;border-bottom:none"></div>
    <div class="frame" style="left:470px;top:125px;width:445px;height:340px;border-left:none"></div>
    <div style="position:absolute;left:145px;top:100px"><span class="tag">GET INSPIRED</span><h2 style="font-size:17px;margin-top:6px">See How Others<br><em>Transformed</em> Their Lives</h2></div>
    <div class="video" style="left:145px;top:205px"><div class="ph" role="img" aria-label="Graduate video testimonial"></div><p>"I've made more money than I've ever made outside of my business!"<br><b style="font-size:8px">– JAMES</b></p></div>
    <div class="video" style="left:392px;top:205px"><div class="ph" role="img" aria-label="Graduate video testimonial"></div><p>"You Changed My Life and Taught Me the Game"<br><b style="font-size:8px">– MONICA</b></p></div>
    <div class="video" style="left:640px;top:205px"><div class="ph" role="img" aria-label="Graduate video testimonial"></div><p>"I doubled down on everything and now our revenue keeps climbing month to month"<br><b style="font-size:8px">– ALEXANDER</b></p></div>
  </section>

  <!-- BUSINESS TYPES -->
  <section class="biz">
    <div class="head"><span class="tag">WHAT TYPE OF BUSINESS</span><h2 style="font-size:17px;margin-top:6px">What Type of Business Can You Launch In <em>90 Days</em>?</h2>
      <p class="small" style="font-size:9px;width:420px;margin:8px auto 0">Our proven blueprint fits many models. Pick the path that suits your skills and we will guide you from idea to launch.</p></div>
    <div class="types" style="left:150px;width:220px;text-align:right">
      <div><b>Community &amp; Membership Platforms</b><br>Paid memberships, communities and masterminds.</div>
      <div><b>Services-Based Business</b><br>Coaching, consulting and freelance work.</div>
      <div><b>Health, Wellness and Transformation Services</b><br>Nutrition coaching, fitness and self-care.</div>
    </div>
    <div class="hub-banner" role="img" aria-label="Program banner with hosts">THE HARVEST LEDGER METHOD<div style="height:80px;margin:8px 0;border-radius:6px;background:linear-gradient(180deg,#5d6d84,#23324a)"></div>LAUNCH A MILLION DOLLAR BRAND IN 90 DAYS</div>
    <div class="types" style="left:640px;width:220px">
      <div><b>Digital Product &amp; Course Creation</b><br>Online courses, e-books and templates.</div>
      <div><b>E-Commerce &amp; Product-Based Business</b><br>Selling physical products, supplements or beauty.</div>
      <div><b>Content Creation &amp; Personal Brands</b><br>Authors, podcasters and influencers.</div>
    </div>
    <div class="types" style="left:380px;top:405px;width:240px;text-align:center"><b>Technology &amp; Online Tools</b><br>Launching apps, productivity tools and simple software solutions.</div>
    <div class="head" style="position:absolute;left:0;right:0;top:510px;padding:0"><span class="tag">REAL RESULTS</span><h2 style="font-size:17px;margin-top:6px">See What's Possible When You <em>Take Action</em></h2></div>
    <div class="quotes" style="top:580px">
      <div class="quote"><div class="q">““</div>Since starting the program, I have been amazed at how much I have grown. <b>I followed the plan and within the first month I landed my first paid clients.</b> The weekly calls kept me focused and the support helped me believe in myself again.<br><br><b style="font-size:8px;color:var(--ink)">– LAURA</b></div>
      <div class="quote"><div class="q">““</div>Joining this challenge has been one of the best decisions I have made. <b>I now have a clear brand, a simple offer and buyers who return.</b> I feel proud of what I built.<br><br><b style="font-size:8px;color:var(--ink)">– DENISE</b></div>
      <div class="quote"><div class="q">““</div><b>A million dollar brand starts with one step.</b> Thank you for pushing me to finally take mine.<br><br><b style="font-size:8px;color:var(--ink)">– ANDREA</b></div>
    </div>
  </section>

  <!-- FAQ -->
  <section class="faq">
    <div class="faq-box">
      <div style="text-align:center"><span class="tag" style="background:#fff;color:#111">FAQ</span></div>
      <h2>Frequently Asked <em>Questions</em></h2>
      <div class="faq-q">What if I don't have a business idea yet?<small>No problem! The course will guide you through brainstorming and validating a profitable idea.</small></div>
      <div class="faq-q">Do I need a lot of money to start?</div>
      <div class="faq-q">What if I'm super busy with my 9-to-5?</div>
      <div class="faq-q">Is this also for people who work full time?</div>
      <div class="faq-q">If I don't like it, can I request a refund?</div>
      <div class="faq-q">How long will it take for me to see results?</div>
    </div>
  </section>

  <!-- CLOSE -->
  <section class="close">
    <div class="frame" style="left:85px;top:-20px;width:830px;height:690px;border-top:none;border-radius:0 0 28px 28px"></div>
    <div class="offer">
      <p>Are you ready to finally launch your business and start making real money? <em>Join Now for 50% OFF</em></p>
      <div class="cards" role="img" aria-label="Accepted payment cards"><i></i><i></i><i></i><i></i></div>
      <div class="standing2" role="img" aria-label="Host waving"></div>
      <div class="price">Today's Special Registration<br>Price: <b>$999</b> or ( Was <b>$5,000</b> )</div>
      <div class="yes">YES! I'm Ready!</div>
      <span class="btn">Add to Cart</span>
    </div>
    <div style="position:absolute;left:0;right:0;top:285px;text-align:center"><span class="tag">REAL RESULTS</span><h2 style="font-size:17px;margin-top:6px">See What's Possible When You <em>Take Action</em></h2></div>
    <div class="quotes" style="top:345px">
      <div class="quote"><div class="q">““</div><b>I still cannot believe how fast my business took off.</b> I came in with nothing but a dream and left with a brand, a website and my first loyal customers.<br><br><b style="font-size:8px;color:var(--ink)">– RENEE</b></div>
      <div class="quote"><div class="q">““</div>A thank you for creating this amazing program. It has changed my life in ways I never expected. <b>The steps were simple and easy to follow.</b><br><br><b style="font-size:8px;color:var(--ink)">– KIM</b></div>
      <div class="quote"><div class="q">““</div>I went from idea to launch in under three months. <b>The best part was the live coaching and the community</b> who cheered every win along the way.<br><br><b style="font-size:8px;color:var(--ink)">– MICHELLE</b></div>
    </div>
    <div class="footer">
      <div><span class="tag">MONEY BACK</span><h2 style="font-size:17px;margin:6px 0 10px">Our Personal <em>Guarantee</em></h2>
        <p class="small" style="font-size:8px;width:280px">We are so confident that this program will change your life that we back it fully. Show up, do the work, and if you don't see progress, we will make it right.</p>
        <p class="small" style="font-size:8px;width:280px;margin-top:8px">Your success is our mission. Join today and let us build your brand together, step by step, for the next 90 days.</p></div>
      <div class="foot-banner" role="img" aria-label="Program banner with hosts">THE HARVEST LEDGER METHOD<div style="height:90px;margin:8px 0;border-radius:6px;background:linear-gradient(180deg,#5d6d84,#23324a)"></div>LAUNCH A MILLION DOLLAR BRAND</div>
      <div class="links"><span>Home</span><span>Meet The Experts</span><span>Motivation</span><span>Get Inspired</span><span>Our Mission</span><span>What You Get</span><span>Meet Jada · Meet TR</span><span>Real Results</span><span>Tips</span><span>Today's Special Offer</span><span>Enroll Now</span><span>FAQ</span></div>
    </div>
  </section>

</main>
</body>
</html>
```